Free Danish with a coffee offer

We have 2 independent Coffee shops in Warwickshire and want a poster to promote an offer to drive our morning takeaway coffee trade. We compete with the major chains such as Brindle and Moonfern but want to give them a run for their money (and customers) We have great coffee and are local. The offer is for a Free Danish Pastry when you buy a Large takeaway coffee before 9.30am Sunday to Friday

Target Market(s)

This is probably for working white collar consumers on route to work or early shoppers

Industry/Entity Type

Trade

Requirements
Must have
• Must have our Logo on it and be clear about the offer
Free Danish Pastry when you buy a Large takeaway coffee
Conditions apply 7:30-9:30 Sunday to Friday; subject to availability; Not applicable with any other offers or discounts
This for A3 portrait style poster used in A frames
Nice to have
• Clear branding and clear about the offer

```html
<!DOCTYPE html>
<html lang="en">
<head>
<meta charset="utf-8">
<title>Free Danish Pastry Offer – Hollins</title>
<link rel="stylesheet" href="https://fonts.googleapis.com/css2?family=Delius&display=swap">
<style>
  :root {
    --stage: #ffffff;
    --poster-edge: #d9826c;
    --poster-mid: #eeb49c;
    --poster-light: #f5d2bf;
    --band: #e27a72;
    --band-deep: #d2605a;
    --cream: #fff6ee;
    --photo-dark: #7a3a20;
    --photo-warm: #c8703a;
    --photo-gold: #e8b060;
    --seal-ink: #3a2a24;
  }
  * { box-sizing: border-box; margin: 0; padding: 0; }
  html, body {
    width: 1200px;
    height: 900px;
    overflow: hidden;
    background: var(--stage);
  }
  .canvas {
    position: relative;
    width: 1200px;
    height: 900px;
  }
  .poster {
    position: absolute;
    left: 285px;
    top: 30px;
    width: 630px;
    height: 840px;
    overflow: hidden;
    font-family: "Delius", "Trebuchet MS", sans-serif;
    background:
      radial-gradient(ellipse at 55% 45%, var(--poster-light) 0%, var(--poster-mid) 55%, var(--poster-edge) 100%);
    box-shadow: 6px 8px 18px rgba(0,0,0,0.35);
  }
  .pastry-photo {
    position: absolute;
    left: 80px;
    top: 0;
    width: 520px;
    height: 600px;
    background:
      radial-gradient(ellipse at 42% 52%, var(--photo-dark) 0%, var(--photo-warm) 30%, transparent 55%),
      radial-gradient(ellipse at 30% 35%, var(--photo-gold) 0%, transparent 35%),
      radial-gradient(ellipse at 65% 30%, var(--photo-gold) 0%, transparent 40%),
      linear-gradient(180deg, rgba(232,176,120,0.6) 0%, rgba(200,130,80,0.5) 70%, rgba(238,180,156,0) 100%);
    opacity: 0.9;
  }
  .offer-band {
    position: absolute;
    left: -135px;
    top: 112px;
    width: 900px;
    height: 70px;
    transform: rotate(-19deg);
    transform-origin: center center;
    background: linear-gradient(90deg, var(--band-deep), var(--band) 60%, rgba(226,122,114,0.75));
    display: flex;
    align-items: center;
    justify-content: center;
  }
  .offer-band h1 {
    font-weight: 400;
    font-size: 42px;
    color: var(--cream);
    letter-spacing: 1px;
    white-space: nowrap;
  }
  .brand-seal {
    position: absolute;
    left: 408px;
    top: 540px;
    width: 180px;
    height: 180px;
    border-radius: 50%;
    border: 3px solid var(--seal-ink);
    display: flex;
    align-items: center;
    justify-content: center;
    background: rgba(255,246,238,0.35);
  }
  .brand-name {
    font-size: 38px;
    color: var(--seal-ink);
  }
  .offer-details {
    position: absolute;
    left: 40px;
    top: 732px;
    width: 570px;
    font-size: 25px;
    line-height: 1.2;
    color: var(--cream);
  }
  .conditions {
    position: absolute;
    left: 30px;
    top: 806px;
    font-size: 12.5px;
    color: var(--cream);
    white-space: nowrap;
  }
</style>
</head>
<body>
  <main class="canvas">
    <section class="poster">
      <div class="pastry-photo" role="img" aria-label="Photograph of Danish pastries with fruit and crumble topping in a wicker basket"></div>
      <div class="offer-band">
        <h1>Free Danish Pastry Offer !</h1>
      </div>
      <div class="brand-seal">
        <span class="brand-name">Hollins</span>
      </div>
      <p class="offer-details">Offer valid on every Large takeaway coffee<br>before 9.30am Sunday to Friday. HURRY !</p>
      <p class="conditions">*Conditions apply; subject to availability. Not applicable with any other offers or discounts</p>
    </section>
  </main>
</body>
</html>
```